Automotive Brand Survey Online

Hi guys, we are looking for a freelancer who can design User Interface design (UI) for a survey-online website layout. <br/><br/>For the content, there are question, choices, back and next buttons - as if you are designing a survey website.<br/><br/>There are 5 main contents of the website consists of:<br/>1. Single-answer question<br/>2. Yes/No-answer question<br/>3. Net Promoter Score (NPS) or 1-5 scale question<br/>4. Open-end question<br/>5. Thank you page when finish survey<br/><br/>Here is the demo and more description<br/>https://preview.quorvane.site/survey/
Target Market(s)
Car Owner
Industry/Entity Type
Automotive
Number of Pages Required
1 page

```html
<!DOCTYPE html>
<html lang="en">
<head>
<meta charset="utf-8">
<title>Survey – Satisfaction Score</title>
<link href="https://fonts.googleapis.com/css2?family=Noto+Sans:wght@400;600;700&display=swap" rel="stylesheet">
<style>
  :root{
    --header-bg:#ebebeb;
    --page-bg:#282828;
    --ink:#2b2b2b;
    --white:#ffffff;
    --teal:#6cc3a0;
    --teal-dark:#4c9a7c;
    --muted:#c9c9c9;
    --choice:#5e3c35;
    --choice-active:#dc694c;
    --back:#243b55;
    --next:#c8143f;
  }
  *{box-sizing:border-box;margin:0;padding:0}
  html,body{width:675px;height:1200px;overflow:hidden}
  body{background:var(--page-bg);font-family:"Noto Sans",sans-serif;position:relative;color:var(--white)}
  .site-header{position:absolute;left:0;top:0;width:675px;height:150px;background:var(--header-bg);box-shadow:0 6px 14px rgba(0,0,0,.35);z-index:2}
  .brand{position:absolute;left:38px;top:62px;display:flex;align-items:center;gap:8px}
  .brand-square{width:14px;height:14px;background:var(--teal)}
  .brand-name{font-weight:700;font-size:20px;color:var(--ink);letter-spacing:.5px}
  .progress-title{position:absolute;left:334px;top:40px;font-size:15px;font-weight:600;color:var(--ink)}
  .progress-title span{margin-left:10px}
  .progress-steps{position:absolute;top:76px;left:0;width:675px;font-size:12px;font-weight:600}
  .progress-steps span{position:absolute;transform:translateX(-50%);color:#d4d4d4}
  .progress-steps .current{color:var(--teal)}
  .progress-steps .goal{color:#9a9a9a}
  .progress-track{position:absolute;left:337px;top:100px;width:300px;height:12px;border:1.5px solid #9a9a9a;border-radius:4px;background:var(--white)}
  .progress-fill{position:absolute;left:2px;top:2.5px;height:4px;width:221px;background:var(--teal);border-radius:2px}
  .progress-dot{position:absolute;top:2px;width:5px;height:5px;border-radius:50%;background:var(--teal-dark);transform:translateX(-50%)}
  .progress-dot.is-end{background:#b5b5b5}
  .question{position:absolute;left:36px;top:215px;font-size:30px;font-weight:700;white-space:nowrap}
  .question .num{color:var(--teal)}
  .gauge{position:absolute;left:0;top:300px}
  .choices{position:absolute;left:37.5px;top:587px;display:flex;gap:19px}
  .choice{width:105px;height:65px;border-radius:8px;background:var(--choice);display:flex;align-items:center;justify-content:center;font-size:21px;font-weight:700}
  .choice.is-selected{background:var(--choice-active)}
  .choice-label{position:absolute;left:0;width:675px;top:693px;text-align:center;font-size:22px;font-weight:600}
  .nav-btn{position:absolute;top:841px;width:219px;height:50px;border-radius:4px;display:flex;align-items:center;justify-content:center;font-size:20px;font-weight:700}
  .nav-back{left:74px;background:var(--back)}
  .nav-next{left:383px;background:var(--next)}
  .nav-next svg{position:absolute;right:16px;top:17px}
</style>
</head>
<body>
  <header class="site-header">
    <div class="brand"><div class="brand-square"></div><div class="brand-name">QUORVA</div></div>
    <div class="progress-title">Your Progress:<span>75% Complete</span></div>
    <div class="progress-steps">
      <span style="left:344px">0%</span>
      <span style="left:415px">25%</span>
      <span style="left:487px">50%</span>
      <span class="current" style="left:559px">75%</span>
      <span class="goal" style="left:631px">100%</span>
    </div>
    <div class="progress-track">
      <div class="progress-fill"></div>
      <div class="progress-dot" style="left:5px"></div>
      <div class="progress-dot" style="left:77px"></div>
      <div class="progress-dot" style="left:149px"></div>
      <div class="progress-dot" style="left:221px"></div>
      <div class="progress-dot is-end" style="left:293px"></div>
    </div>
  </header>

  <h1 class="question"><span class="num">S4.</span> Please rate your satisfaction score.</h1>

  <svg class="gauge" width="675" height="260" viewBox="0 0 675 260" aria-label="Satisfaction gauge showing 5">
    <defs>
      <linearGradient id="needle-shade" x1="0" y1="-7" x2="0" y2="7" gradientUnits="userSpaceOnUse">
        <stop offset="0" stop-color="#ffffff"/>
        <stop offset="1" stop-color="#cfcfcf"/>
      </linearGradient>
    </defs>
    <g transform="translate(336 188)" stroke-linecap="round" stroke="#fff">
      <line x1="126" x2="147" stroke-width="9" transform="rotate(-186)"/>
      <line x1="133" x2="147" stroke-width="5" transform="rotate(-178.3)"/>
      <line x1="128" x2="147" stroke-width="7" transform="rotate(-170.6)"/>
      <line x1="133" x2="147" stroke-width="5" transform="rotate(-163)"/>
      <line x1="128" x2="147" stroke-width="7" transform="rotate(-155.3)"/>
      <line x1="133" x2="147" stroke-width="5" transform="rotate(-147.6)"/>
      <line x1="128" x2="147" stroke-width="7" transform="rotate(-139.9)"/>
      <line x1="133" x2="147" stroke-width="5" transform="rotate(-132.2)"/>
      <line x1="128" x2="147" stroke-width="7" transform="rotate(-124.6)"/>
      <line x1="133" x2="147" stroke-width="5" transform="rotate(-116.9)"/>
      <line x1="128" x2="147" stroke-width="7" transform="rotate(-109.2)"/>
      <line x1="133" x2="147" stroke-width="5" transform="rotate(-101.5)"/>
      <line x1="126" x2="147" stroke-width="9" transform="rotate(-93.8)"/>
      <line x1="133" x2="147" stroke-width="5" transform="rotate(-86.2)"/>
      <line x1="128" x2="147" stroke-width="7" transform="rotate(-78.5)"/>
      <line x1="133" x2="147" stroke-width="5" transform="rotate(-70.8)"/>
      <line x1="128" x2="147" stroke-width="7" transform="rotate(-63.1)"/>
      <line x1="133" x2="147" stroke-width="5" transform="rotate(-55.4)"/>
      <line x1="128" x2="147" stroke-width="7" transform="rotate(-47.8)"/>
      <line x1="133" x2="147" stroke-width="5" transform="rotate(-40.1)"/>
      <line x1="128" x2="147" stroke-width="7" stroke="#f07030" transform="rotate(-32.4)"/>
      <line x1="133" x2="147" stroke-width="5" stroke="#f05a30" transform="rotate(-24.7)"/>
      <line x1="128" x2="147" stroke-width="7" stroke="#ee3035" transform="rotate(-17)"/>
      <line x1="133" x2="147" stroke-width="5" stroke="#ee3035" transform="rotate(-9.4)"/>
      <line x1="126" x2="147" stroke-width="9" stroke="#ee3035" transform="rotate(-1.7)"/>
      <line x1="133" x2="147" stroke-width="5" stroke="#ee3035" transform="rotate(6)"/>
    </g>
    <g transform="translate(336 188)" fill="#fff" font-family="Noto Sans, sans-serif" font-weight="700" font-size="21" text-anchor="middle" dominant-baseline="central">
      <text x="-167" y="20">0</text>
      <text x="-145" y="-90">1</text>
      <text x="-56" y="-165">2</text>
      <text x="58" y="-165">3</text>
      <text x="147" y="-90">4</text>
      <text x="168" y="20">5</text>
    </g>
    <g class="gauge-needle" transform="translate(336 188) rotate(6.4)">
      <path d="M0,-7.5 L113,-3.5 A3.5,3.5 0 0 1 113,3.5 L0,7.5 Z" fill="url(#needle-shade)" stroke="#bdbdbd" stroke-width="1"/>
      <circle r="22" fill="#fff" stroke="#cfcfcf" stroke-width="1.5"/>
      <circle r="15" fill="none" stroke="#e2e2e2" stroke-width="2"/>
      <circle r="8.5" fill="#4db3f0"/>
    </g>
  </svg>

  <div class="choices">
    <div class="choice">1</div>
    <div class="choice">2</div>
    <div class="choice">3</div>
    <div class="choice">4</div>
    <div class="choice is-selected">5</div>
  </div>
  <p class="choice-label">Very Satisfied</p>

  <div class="nav-btn nav-back">BACK</div>
  <div class="nav-btn nav-next">NEXT
    <svg width="10" height="17" viewBox="0 0 10 17"><polyline points="1.5,1.5 8.5,8.5 1.5,15.5" fill="none" stroke="#fff" stroke-width="2.2" stroke-linecap="round" stroke-linejoin="round"/></svg>
  </div>
</body>
</html>
```